Lydia Hartwell personal business/name cards and stationery brief

I am looking for a simple design on my personal business cards, that I may use for all my stationery. All my stationery would be cream or ivory textured card, or cream/ivory quality paper. I am director of my family company and also property developer. But am wishing to have basic business cards that I can use across both businesses. I do not wish to have a title, just my initials as a focal point.
Target Market(s)
These are my personal business cards and stationery. I am looking for an elegant, relatively understated design that exudes wealth. There is no target audience, other than clients or people I already do business with. However design must be stylish and timeless.
If I am handing out my business card to anyone I do not do business with, or they are not contracting to me or my company currently, then i would like the target audience to wish they were.
I am 54 yeas of age, and my business cards must denote respect and class.
Industry/Entity Type
Business
Contact Information for Business Card
LH
Lydia Hartwell
Justice of the Peace
Possible rear of card
Mobile number
Email
Font styles to use
Requirements
Must have
- LH to be somehow entwined as a logo on the front of the card above my name
- These cards must state that I am a Justice of the Peace
- Colours only ivory or cream card with texture, and gold elegant font.
- Must be able to be used on all my stationery products
- Must be elegant, timeless and not cluttered
- Below are just some design I like. There is something in each design I like.
Nice to have
- I would like my initials to be the centre piece of the card. Somehow entwined together elegantly in a logo of sorts that I can use across all my stationery. But if not my initials, then something that is different and stands out from the rest.
Should not have
- Not gawdy or young. No colour. Nothing outlandish.

```html
<!DOCTYPE html>
<html lang="en">
<head>
<meta charset="utf-8">
<title>Lydia Hartwell — Business Cards</title>
<link href="https://fonts.googleapis.com/css2?family=Josefin+Sans:wght@300;400;700&family=Open+Sans:wght@400&display=swap" rel="stylesheet">
<style>
  :root {
    --backdrop: #3f352f;
    --card-white: #ffffff;
    --card-ivory: #fbfaf0;
    --gold: #f3d34a;
    --gold-soft: #f7dc8a;
    --ink: #231f1c;
    --rule: #6d6a64;
  }
  html, body {
    margin: 0;
    padding: 0;
    width: 1200px;
    height: 1200px;
    overflow: hidden;
    background: var(--backdrop);
  }
  .canvas {
    position: relative;
    width: 1200px;
    height: 1200px;
  }
  .card {
    position: absolute;
    width: 700px;
    height: 400px;
    box-sizing: border-box;
    box-shadow: 0 8px 22px rgba(0,0,0,0.35);
  }
  /* Front of card */
  .card-front {
    left: 250px;
    top: 120px;
    background: var(--card-white);
    display: flex;
    flex-direction: column;
    align-items: center;
    justify-content: center;
    font-family: "Josefin Sans", sans-serif;
    color: var(--gold);
  }
  .front-monogram {
    font-family: "Josefin Sans", sans-serif;
    font-weight: 400;
    font-size: 96px;
    letter-spacing: 6px;
    color: var(--gold-soft);
    line-height: 1;
    margin-bottom: 28px;
  }
  .front-name {
    font-weight: 300;
    font-size: 40px;
    letter-spacing: 5px;
    text-transform: uppercase;
    margin: 0;
  }
  .front-title {
    font-weight: 300;
    font-size: 20px;
    letter-spacing: 2px;
    margin: 10px 0 18px;
  }
  .front-rule {
    width: 170px;
    height: 2px;
    background: var(--gold-soft);
  }
  /* Back of card */
  .card-back {
    left: 250px;
    top: 660px;
    background: var(--card-ivory);
    display: flex;
    align-items: center;
    padding: 0 60px 0 80px;
  }
  .back-monogram {
    width: 190px;
    text-align: center;
    font-family: "Josefin Sans", sans-serif;
    font-weight: 700;
    font-size: 88px;
    letter-spacing: 4px;
    color: var(--ink);
  }
  .back-divider {
    width: 1px;
    height: 150px;
    background: var(--rule);
    margin: 0 34px 0 30px;
  }
  .back-details {
    display: flex;
    flex-direction: column;
    gap: 12px;
  }
  .back-name {
    font-family: "Josefin Sans", sans-serif;
    font-weight: 700;
    font-size: 32px;
    letter-spacing: 4px;
    text-transform: uppercase;
    color: var(--ink);
    margin: 0 0 6px;
  }
  .contact-line {
    display: flex;
    align-items: center;
    gap: 12px;
    font-family: "Open Sans", sans-serif;
    font-size: 22px;
    color: var(--ink);
  }
  .contact-icon {
    width: 22px;
    height: 22px;
    flex: none;
  }
</style>
</head>
<body>
<main class="canvas">
  <section class="card card-front" aria-label="Card front">
    <div class="front-monogram">LH</div>
    <h1 class="front-name">Lydia Hartwell</h1>
    <p class="front-title">Justice of the Peace</p>
    <div class="front-rule"></div>
  </section>

  <section class="card card-back" aria-label="Card back">
    <div class="back-monogram">LH</div>
    <div class="back-divider"></div>
    <div class="back-details">
      <h2 class="back-name">Lydia Hartwell</h2>
      <div class="contact-line">
        <svg class="contact-icon" viewBox="0 0 22 22" aria-hidden="true">
          <rect x="1" y="1" width="20" height="20" rx="3" fill="#f3d34a"/>
          <rect x="7.5" y="4" width="7" height="14" rx="1.2" fill="none" stroke="#231f1c" stroke-width="1.4"/>
          <circle cx="11" cy="15.5" r="0.9" fill="#231f1c"/>
        </svg>
        <span>1-555-014-2290</span>
      </div>
      <div class="contact-line">
        <svg class="contact-icon" viewBox="0 0 22 22" aria-hidden="true">
          <rect x="1" y="1" width="20" height="20" rx="3" fill="#f3d34a"/>
          <rect x="4.5" y="6.5" width="13" height="9" fill="#231f1c"/>
          <path d="M4.5 6.5 L11 11.5 L17.5 6.5" fill="none" stroke="#f3d34a" stroke-width="1.2"/>
        </svg>
        <span>lydia@hartwellhouse.com</span>
      </div>
    </div>
  </section>
</main>
</body>
</html>
```